Job type:
Email marketing

Task description:
We are looking to release some email marketing with a value based focus around our new pricing system with an overall aim to generate more interest.
Here is a link to the LMR website - http://www.lumarooms.com/

Copy for email marketing:
Luma Rooms

We’ve ripped up the rule book!

We know the standard is to charge for a whole evening or a full day at a viewing facility, but we just thought it needed to be a bit more straightforward, so we have introduced new hourly rates that will help you get the value you need out of your stretched research budget!

Call us now on 0121 598 6270 for our new rates or complete our enquiry form to receive full details….

Luma Rooms – Fernbrook – Birmingham- UK

Enquiry link below:
http://www.lumarooms.com/focus-group-studios-book.php

Logo text:
LMR

Descriptive words:
Professional
Modern
Playful
Bold

Requirements:
Needs to be uploaded to Post Finch which will require HTML coding

Target Market(s)

The target for the email marketing is Market Research agencies that will book LMR as a venue for focus groups, meetings etc.

Industry/Entity Type

Marketing

Requirements
Must have
• It will need to be uploaded to Post Finch

```html
<!DOCTYPE html>
<html lang="en">
<head>
<meta charset="utf-8">
<title>Luma Rooms – New Hourly Rates</title>
<link href="https://fonts.googleapis.com/css2?family=PT+Sans:wght@400;700&family=Arimo:wght@400;700&display=swap" rel="stylesheet">
<style>
  :root {
    --page-bg: #dedede;
    --sheet-white: #ffffff;
    --brand-yellow: #ffd200;
    --brand-grey: #555b60;
    --charcoal: #333333;
    --ink: #111111;
    --link-blue: #0b2a8a;
    --text-light: #f4f4f4;
  }
  * { box-sizing: border-box; margin: 0; padding: 0; }
  html, body {
    width: 1200px; height: 1000px; overflow: hidden;
    background: var(--page-bg);
    font-family: "PT Sans", sans-serif;
  }
  .email {
    position: absolute; left: 270px; top: 55px;
    width: 660px; height: 888px;
    background: var(--sheet-white);
    overflow: hidden;
  }
  .email-header {
    height: 62px; display: flex; align-items: center; justify-content: space-between;
    padding: 0 20px 0 22px;
  }
  .brand { display: flex; align-items: center; gap: 8px; }
  .brand-dot { width: 44px; height: 44px; border-radius: 50%; background: var(--brand-yellow); }
  .brand-name { font-weight: 700; font-size: 28px; color: var(--brand-grey); letter-spacing: 1px; }
  .site-link {
    font-family: "Arimo", sans-serif; font-size: 15px; color: var(--link-blue);
    text-decoration: underline;
  }
  .rule-yellow { height: 4px; background: var(--brand-yellow); }
  .hero {
    position: relative; height: 180px;
    background: linear-gradient(180deg, #bdbdbd 0%, #eeeeee 35%, #d9d9d9 70%, #a9a9a9 100%);
    display: flex; align-items: center; justify-content: center;
  }
  .hero-title {
    font-weight: 700; font-size: 33px; color: var(--ink); letter-spacing: -0.3px;
    text-shadow: 0 1px 2px rgba(255,255,255,.8);
  }
  .gallery {
    display: grid; grid-template-columns: 314px 346px; grid-template-rows: 240px 280px;
  }
  .photo-meeting-green { background: linear-gradient(135deg, #b9d23a 0%, #d8c9a3 55%, #c49a5f 100%); }
  .photo-boardroom { background: linear-gradient(135deg, #e7ecef 0%, #c7ced4 50%, #3a3a3a 100%); }
  .photo-round-table { background: linear-gradient(135deg, #6f8f3a 0%, #e2dfd8 45%, #c89a5c 75%, #2b2b2b 100%); }
  .photo-office { background: linear-gradient(135deg, #f0f0f0 0%, #d8dadc 55%, #3c3c3c 100%); }
  .offer-circle {
    position: absolute; left: 160px; top: 342px;
    width: 340px; height: 340px; border-radius: 50%;
    border: 3px solid rgba(255,255,255,.9);
    padding: 8px;
  }
  .offer-inner {
    width: 100%; height: 100%; border-radius: 50%; background: var(--charcoal);
    display: flex; flex-direction: column; align-items: center; padding: 26px 38px 0;
    text-align: center;
  }
  .offer-brand { display: flex; align-items: center; gap: 8px; margin-bottom: 14px; }
  .offer-brand .brand-dot { width: 46px; height: 46px; }
  .offer-brand .brand-name { color: #d9d9d9; font-size: 30px; }
  .offer-copy { color: var(--text-light); font-size: 13.4px; line-height: 1.35; text-align: justify; text-align-last: center; }
  .cta {
    margin-top: 14px; display: inline-block; padding: 4px 12px;
    background: var(--brand-yellow); border-radius: 4px; border: 1px solid #c9a400;
    font-family: "Arimo", sans-serif; font-weight: 700; font-size: 18px; color: var(--ink);
    text-decoration: none;
  }
  .divider-band { height: 22px; background: linear-gradient(180deg, #ffffff 0%, #d4d4d4 100%); }
  .rule-yellow.thick { height: 5px; }
  .email-footer {
    height: 95px; background: var(--charcoal); color: var(--text-light);
    display: flex; align-items: flex-start; padding: 18px 16px 0 18px;
  }
  .contact { display: flex; gap: 10px; width: 318px; }
  .contact-icon { flex: none; margin-top: 2px; }
  .contact-text { font-size: 15px; line-height: 1.3; }
  .contact-text strong { font-size: 19px; }
  .footer-sep { width: 1px; height: 42px; background: #6a6a6a; margin: 0 14px 0 4px; }
  .footer-right { flex: 1; text-align: right; padding-right: 14px; }
  .address { font-size: 14px; }
  .social { margin-top: 12px; font-family: "Arimo", sans-serif; font-size: 12px; display: flex; justify-content: flex-end; gap: 16px; }
  .social a { color: var(--text-light); text-decoration: none; }
</style>
</head>
<body>
  <main class="email">
    <header class="email-header">
      <div class="brand"><span class="brand-dot"></span><span class="brand-name">LMR</span></div>
      <a class="site-link" href="http://www.lumarooms.com/">Visit our website</a>
    </header>
    <div class="rule-yellow"></div>

    <section class="hero" role="img" aria-label="Torn paper strip over a greyscale open rule book">
      <h1 class="hero-title">WE’VE RIPPED UP THE RULE BOOK!</h1>
    </section>

    <section class="gallery">
      <div class="photo-meeting-green" role="img" aria-label="Meeting room with lime green wall, wooden table and wall screen"></div>
      <div class="photo-boardroom" role="img" aria-label="Boardroom with black leather chairs and an orange accent wall"></div>
      <div class="photo-round-table" role="img" aria-label="Round meeting table with pink flowers and a palm plant"></div>
      <div class="photo-office" role="img" aria-label="Small viewing office with desk, computer and leather chair"></div>
    </section>

    <div class="offer-circle">
      <div class="offer-inner">
        <div class="offer-brand"><span class="brand-dot"></span><span class="brand-name">LMR</span></div>
        <p class="offer-copy">We know the standard is to charge for a whole evening or a full day at a viewing facility, but we just thought it needed to be a bit more straightforward, so we have introduced new hourly rates that will help you get the value you need out of your stretched research budget!</p>
        <a class="cta" href="http://www.lumarooms.com/focus-group-studios-book.php">Booking now!</a>
      </div>
    </div>

    <div class="divider-band"></div>
    <div class="rule-yellow thick"></div>

    <footer class="email-footer">
      <div class="contact">
        <svg class="contact-icon" width="24" height="24" viewBox="0 0 24 24" aria-hidden="true">
          <circle cx="12" cy="12" r="11" fill="none" stroke="#f4f4f4" stroke-width="1.5"/>
          <path d="M8.5 6.5c.6-.5 1.3-.4 1.7.2l1 1.6c.3.5.2 1.1-.2 1.4l-.7.6c.5 1.3 1.4 2.4 2.6 3.2l.7-.5c.5-.3 1.1-.2 1.4.2l1.1 1.5c.4.6.2 1.3-.4 1.7-2.6 1.7-8.6-4.6-7.2-9.9z" fill="#f4f4f4"/>
        </svg>
        <p class="contact-text">Call us now on <strong>0121 598 6270</strong> for our new rates or complete our enquiry form to receive full details</p>
      </div>
      <div class="footer-sep"></div>
      <div class="footer-right">
        <p class="address">Luma Rooms – Fernbrook – Birmingham- UK</p>
        <div class="social"><a href="#">Chirper</a><a href="#">Friendbook</a></div>
      </div>
    </footer>
  </main>
</body>
</html>
```